Tincture bottle labels

I need my labels slightly adjusted to replace the ingredients part with the supplement facts as shown in the 3 Fernhollow labels attached, for the other 2 it will have to be copied and add an BQC disclosure on the label as well possibly below the storage info near the bottom of the label

Target Market(s)

Everyone

Industry/Entity Type

Vitamins & Supplements

Requirements
Must have
• Supplement facts box and info for each product and BQC disclosures

```html
<!DOCTYPE html>
<html lang="en">
<head>
<meta charset="utf-8">
<title>Fernhollow Liquid Drops Labels</title>
<link href="https://fonts.googleapis.com/css2?family=Luckiest+Guy&family=Open+Sans:ital,wght@0,400;0,600;0,700;0,800;1,800&display=swap" rel="stylesheet">
<style>
:root{
  --ink:#111;
  --paper:#fff;
  --brick:#9c4a2c;
  --orange:#f06a22;
  --green:#3aa935;
  --forest:#2f8a5a;
  --yellow:#f3c316;
  --sky:#7d9dd6;
  --red:#e2242a;
  --ice:#5aa9e2;
  --tangerine:#f1641f;
  --violet:#5b3a9a;
  --cyan:#1c97d6;
}
*{box-sizing:border-box;margin:0;padding:0}
html,body{width:1200px;height:2268px;overflow:hidden;background:#fff}
body{font-family:"Open Sans",sans-serif;color:var(--ink)}
.sheet{width:1200px;height:2268px;display:flex;flex-direction:column}
.label{position:relative;width:1200px;height:453.6px;overflow:hidden}
.label--lions-mane{--band:var(--orange);--accent:var(--green);--photo-a:#e9dcc7;--photo-b:#6b5a4a}
.label--turkey-tail{--band:var(--forest);--accent:var(--yellow);--photo-a:#c9782f;--photo-b:#5a4a3e}
.label--reishi{--band:var(--sky);--accent:var(--red);--photo-a:#b8532b;--photo-b:#7a3020}
.label--chaga{--band:var(--ice);--accent:var(--tangerine);--photo-a:#6a4b33;--photo-b:#2e2622}
.label--cordyceps{--band:var(--violet);--accent:var(--cyan);--photo-a:#f08a1e;--photo-b:#7a4a14}

.photo{position:absolute;left:0;top:0;width:1200px;height:360px;background:linear-gradient(120deg,var(--photo-b),var(--photo-a) 55%,var(--photo-b))}
.band{position:absolute;left:0;top:0;width:1200px;height:360px}
.band path{fill:var(--band)}
.rule{position:absolute;left:0;top:352px;width:1200px;height:9px;background:var(--accent)}
.bricks{position:absolute;left:0;top:361px;width:1200px;height:93px;background:var(--brick)}

.maker{position:absolute;left:46px;top:48px;writing-mode:vertical-rl;font-size:10px;line-height:14px;color:rgba(255,255,255,.85)}
.maker strong{font-weight:800;text-transform:uppercase;font-size:9px}
.site{position:absolute;left:60px;top:180px;writing-mode:vertical-rl;font-size:11px;color:rgba(255,255,255,.85)}

.facts{position:absolute;left:107px;top:45px;width:205px;height:340px;background:var(--paper);border:3px solid var(--ink);border-radius:14px;box-shadow:4px 4px 0 var(--ink);padding:6px 8px;text-align:center;font-size:9.5px;line-height:12.5px}
.facts h3{font-family:"Luckiest Guy",sans-serif;font-weight:400;font-size:17px;line-height:20px;letter-spacing:.3px;text-align:left;padding-left:8px}
.facts .meta{text-align:left;padding-left:12px;font-size:9.5px;border-bottom:4px solid var(--ink);padding-bottom:2px}
.facts .amount{display:flex;justify-content:flex-end;gap:10px;font-weight:800;font-size:9.5px;border-bottom:1px solid var(--ink);padding:3px 4px 2px}
.facts .ingredient{border-bottom:2px solid var(--ink);padding:3px 0}
.facts .dv{border-bottom:2px solid var(--ink);padding:2px 0 3px}
.facts h4{font-family:"Luckiest Guy",sans-serif;font-weight:400;font-size:15px;line-height:18px;margin-top:4px}
.facts .notice{border:1px solid var(--ink);margin:4px 6px 0;padding:2px 3px;font-size:9px;line-height:12px}

.shroom{position:absolute;width:36px;height:42px;border-radius:50% 50% 30% 30%;background:var(--red)}
.shroom--a{left:28px;top:318px}
.shroom--b{left:318px;top:318px}
.shroom--c{left:728px;top:318px}

.brand{position:absolute;left:450px;top:60px;width:300px;display:flex;align-items:center;justify-content:center;gap:12px;flex-direction:column}
.brand .dot{width:110px;height:110px;border-radius:50%;background:var(--accent)}
.brand .name{font-family:"Luckiest Guy",sans-serif;font-size:48px;line-height:52px;color:var(--accent)}
.product{position:absolute;left:400px;top:256px;width:400px;text-align:center;font-family:"Luckiest Guy",sans-serif;font-size:40px;letter-spacing:1.5px;color:#fff;-webkit-text-stroke:1.5px #333;text-shadow:2px 2px 0 #333}
.pill{position:absolute;left:490px;top:330px;width:220px;height:54px;border-radius:27px;background:var(--accent);color:#fff;font-size:22px;display:flex;align-items:center;justify-content:center}
.volume{position:absolute;left:400px;top:400px;width:400px;text-align:center;font-weight:800;font-size:20px;color:#fff;letter-spacing:1px}

.benefits{position:absolute;left:912px;top:42px;width:215px;height:343px;background:var(--paper);border:3px solid var(--ink);border-radius:14px;box-shadow:5px 5px 0 var(--ink);padding:22px 14px 10px}
.benefits h2{font-family:"Luckiest Guy",sans-serif;font-weight:400;color:var(--accent);font-size:22px;line-height:31px;text-align:center;letter-spacing:.5px}
.benefits h5{font-family:"Luckiest Guy",sans-serif;font-weight:400;font-size:19px;text-align:center;margin-top:14px}
.benefits ul{list-style:none;padding-left:18px;margin-top:4px}
.benefits li{position:relative;font-weight:800;font-style:italic;font-size:16px;line-height:18px;text-transform:uppercase;margin-bottom:8px}
.benefits li::before{content:"";position:absolute;left:-15px;top:9px;width:5px;height:5px;border-radius:50%;background:var(--ink)}
.benefits .icon{display:block;margin:6px auto 0;width:36px;height:40px;border-radius:50% 50% 30% 30%;background:var(--accent)}
</style>
</head>
<body>
<main class="sheet">

<section class="label label--lions-mane">
  <div class="photo" role="img" aria-label="Photo of white lion's mane mushroom"></div>
  <svg class="band" viewBox="0 0 1200 360"><path d="M0 28 C300 20 420 60 600 170 L1200 170 L1200 360 L0 360 Z"/></svg>
  <div class="rule"></div>
  <div class="bricks" role="img" aria-label="Brick wall pattern"></div>
  <p class="maker"><strong>Manufactured by:</strong><br>Fernhollow LLC<br>Bayview, Florida</p>
  <p class="site">fernhollow.shop</p>
  <div class="shroom shroom--a" role="img" aria-label="Red spotted mushroom illustration"></div>
  <div class="shroom shroom--b" role="img" aria-label="Red spotted mushroom illustration"></div>
  <div class="shroom shroom--c" role="img" aria-label="Red spotted mushroom illustration"></div>
  <div class="facts">
    <h3>Supplement Facts</h3>
    <p class="meta">Serving Size: 2 droppers (2mL)<br>Servings Per Container: About 30</p>
    <p class="amount"><span>AMOUNT PER SERVING</span><span>2mL*</span></p>
    <p class="ingredient">Organic Lion's Mane (Hericium Erinaceus), fruitbody extract, cane alcohol, water</p>
    <p class="dv">Daily value not establised</p>
    <h4>Suggested Use:</h4>
    <p>Take 1-2 ml daily or as directed by your healthcare provider. Consume directly or add to beverages for a cognitive boost.</p>
    <h4>Storage:</h4>
    <p>Store in a cool, dry place away from sunlight.</p>
    <p class="notice">These statements have not been evaluated by the Board of Quality Control. This product is not intended to diagnose, treat, cure or prevent any disease.</p>
  </div>
  <div class="brand"><span class="dot"></span><span class="name">Fernhollow</span></div>
  <p class="product">Lion's Mane</p>
  <p class="pill">LIQUID DROPS</p>
  <p class="volume">2 fl. oz / (60 ml)</p>
  <div class="benefits">
    <h2>Enhance Memory, Focus, &amp; Nerve Health</h2>
    <h5>Key Benefits:</h5>
    <ul><li>Supports brain health</li><li>Cognitive function</li><li>Nerve regeneration</li></ul>
    <span class="icon" role="img" aria-label="Small mushroom illustration"></span>
  </div>
</section>

<section class="label label--turkey-tail">
  <div class="photo" role="img" aria-label="Photo of turkey tail mushroom"></div>
  <svg class="band" viewBox="0 0 1200 360"><path d="M0 28 C300 20 420 60 600 150 L1200 150 L1200 360 L0 360 Z"/></svg>
  <div class="rule"></div>
  <div class="bricks" role="img" aria-label="Brick wall pattern"></div>
  <p class="maker"><strong>Manufactured by:</strong><br>Fernhollow LLC<br>Bayview, Florida</p>
  <p class="site">fernhollow.shop</p>
  <div class="shroom shroom--b" role="img" aria-label="Red spotted mushroom illustration"></div>
  <div class="shroom shroom--c" role="img" aria-label="Red spotted mushroom illustration"></div>
  <div class="facts">
    <h3>Supplement Facts</h3>
    <p class="meta">Serving Size: 2 droppers (2mL)<br>Servings Per Container: About 30</p>
    <p class="amount"><span>AMOUNT PER SERVING</span><span>2mL*</span></p>
    <p class="ingredient">Organic Turkey Tail (Trametes Versicolor) fruitbody extract, cane alcohol, water</p>
    <p class="dv">Daily value not establised</p>
    <h4>Suggested Use:</h4>
    <p>Take 1-2 ml daily or as directed by your healthcare provider. Consume directly or add to beverages for a cognitive boost.</p>
    <h4>Storage:</h4>
    <p>Store in a cool, dry place away from sunlight.</p>
    <p class="notice">These statements have not been evaluated by the Board of Quality Control. This product is not intended to diagnose, treat, cure or prevent any disease.</p>
  </div>
  <div class="brand"><span class="dot"></span><span class="name">Fernhollow</span></div>
  <p class="product">Turkey Tail</p>
  <p class="pill">LIQUID DROPS</p>
  <p class="volume">2 fl. oz / (60 ml)</p>
  <div class="benefits">
    <h2>Nourish Your Gut &amp; Strengthen Immunity</h2>
    <h5>Key Benefits:</h5>
    <ul><li>Supports digestive health</li><li>Immune system balance</li></ul>
    <span class="icon" role="img" aria-label="Small mushroom illustration"></span>
  </div>
</section>

<section class="label label--reishi">
  <div class="photo" role="img" aria-label="Photo of reishi mushroom"></div>
  <svg class="band" viewBox="0 0 1200 360"><path d="M0 28 C300 20 420 60 600 150 L1200 150 L1200 360 L0 360 Z"/></svg>
  <div class="rule"></div>
  <div class="bricks" role="img" aria-label="Brick wall pattern"></div>
  <p class="maker"><strong>Manufactured by:</strong><br>Fernhollow LLC<br>Bayview, Florida</p>
  <p class="site">fernhollow.shop</p>
  <div class="shroom shroom--b" role="img" aria-label="Red spotted mushroom illustration"></div>
  <div class="shroom shroom--c" role="img" aria-label="Red spotted mushroom illustration"></div>
  <div class="facts">
    <h3>Supplement Facts</h3>
    <p class="meta">Serving Size: 2 droppers (2mL)<br>Servings Per Container: About 30</p>
    <p class="amount"><span>AMOUNT PER SERVING</span><span>2mL*</span></p>
    <p class="ingredient">Organic Reishi (Ganoderma lucidum) fruitbody extract, cane alcohol, water</p>
    <p class="dv">Daily value not establised</p>
    <h4>Suggested Use:</h4>
    <p>Take 1-2 ml daily or as directed by your healthcare provider. Consume directly or add to beverages for a cognitive boost.</p>
    <h4>Storage:</h4>
    <p>Store in a cool, dry place away from sunlight.</p>
    <p class="notice">These statements have not been evaluated by the Board of Quality Control. This product is not intended to diagnose, treat, cure or prevent any disease.</p>
  </div>
  <div class="brand"><span class="dot"></span><span class="name">Fernhollow</span></div>
  <p class="product">Reishi</p>
  <p class="pill">LIQUID DROPS</p>
  <p class="volume">2 fl. oz / (60 ml)</p>
  <div class="benefits">
    <h2>Calm Your Mind &amp; Fortify Your Immune System</h2>
    <h5>Key Benefits:</h5>
    <ul><li>Supports immunity</li><li>Stress reduction</li><li>Overall wellness</li></ul>
    <span class="icon" role="img" aria-label="Small mushroom illustration"></span>
  </div>
</section>

<section class="label label--chaga">
  <div class="photo" role="img" aria-label="Photo of chaga mushroom on bark"></div>
  <svg class="band" viewBox="0 0 1200 360"><path d="M0 28 C300 20 420 60 600 150 L1200 150 L1200 360 L0 360 Z"/></svg>
  <div class="rule"></div>
  <div class="bricks" role="img" aria-label="Brick wall pattern"></div>
  <p class="maker"><strong>Manufactured by:</strong><br>Fernhollow LLC<br>Bayview, Florida</p>
  <p class="site">fernhollow.shop</p>
  <div class="shroom shroom--b" role="img" aria-label="Red spotted mushroom illustration"></div>
  <div class="shroom shroom--c" role="img" aria-label="Red spotted mushroom illustration"></div>
  <div class="facts">
    <h3>Supplement Facts</h3>
    <p class="meta">Serving Size: 2 droppers (2mL)<br>Servings Per Container: About 30</p>
    <p class="amount"><span>AMOUNT PER SERVING</span><span>2mL*</span></p>
    <p class="ingredient">Organic Chaga (Inonotus obliquus), fruitbody extract, cane alcohol, water</p>
    <p class="dv">Daily value not establised</p>
    <h4>Suggested Use:</h4>
    <p>Take 1-2 ml daily or as directed by your healthcare provider. Consume directly or add to beverages for a cognitive boost.</p>
    <h4>Storage:</h4>
    <p>Store in a cool, dry place away from sunlight.</p>
    <p class="notice">These statements have not been evaluated by the Board of Quality Control. This product is not intended to diagnose, treat, cure or prevent any disease.</p>
  </div>
  <div class="brand"><span class="dot"></span><span class="name">Fernhollow</span></div>
  <p class="product">Chaga</p>
  <p class="pill">LIQUID DROPS</p>
  <p class="volume">2 fl. oz / (60 ml)</p>
  <div class="benefits">
    <h2>Protect and Rejuvenate Your Body</h2>
    <h5 style="margin-top:34px">Key Benefits:</h5>
    <ul><li>Antioxidant-rich for anti-aging</li><li>Immune support</li></ul>
    <span class="icon" role="img" aria-label="Small mushroom illustration" style="margin-top:20px"></span>
  </div>
</section>

<section class="label label--cordyceps">
  <div class="photo" role="img" aria-label="Photo of orange cordyceps mushrooms"></div>
  <svg class="band" viewBox="0 0 1200 360"><path d="M0 28 C300 20 420 60 600 150 L1200 150 L1200 360 L0 360 Z"/></svg>
  <div class="rule"></div>
  <div class="bricks" role="img" aria-label="Brick wall pattern"></div>
  <p class="maker"><strong>Manufactured by:</strong><br>Fernhollow LLC<br>Bayview, Florida</p>
  <p class="site">fernhollow.shop</p>
  <div class="shroom shroom--b" role="img" aria-label="Red spotted mushroom illustration"></div>
  <div class="shroom shroom--c" role="img" aria-label="Red spotted mushroom illustration"></div>
  <div class="facts">
    <h3>Supplement Facts</h3>
    <p class="meta">Serving Size: 2 droppers (2mL)<br>Servings Per Container: About 30</p>
    <p class="amount"><span>AMOUNT PER SERVING</span><span>2mL*</span></p>
    <p class="ingredient">Organic Cordyceps (Cordyceps Militaris) fruitbody extract, cane alcohol, spring water, alcohol content -20%</p>
    <p class="dv">Daily value not establised</p>
    <h4>Suggested Use:</h4>
    <p>Take 1-2 ml daily or as directed by your healthcare provider. Consume directly or add to beverages for a cognitive boost.</p>
    <h4>Storage:</h4>
    <p>Store in a cool, dry place away from sunlight.</p>
    <p class="notice">These statements have not been evaluated by the Board of Quality Control. This product is not intended to diagnose, treat, cure or prevent any disease.</p>
  </div>
  <div class="brand"><span class="dot"></span><span class="name">Fernhollow</span></div>
  <p class="product">Cordyceps</p>
  <p class="pill">LIQUID DROPS</p>
  <p class="volume">2 fl. oz / (60 ml)</p>
  <div class="benefits">
    <h2>Boost Energy and Improve Endurance</h2>
    <h5>Key Benefits:</h5>
    <ul><li>Enhances energy</li><li>Stamina</li><li>Oxygen utilization</li></ul>
    <span class="icon" role="img" aria-label="Small mushroom illustration"></span>
  </div>
</section>

</main>
</body>
</html>
```